Carrowfield Banner- Real Estate Luxury Sale Banner

I need a large banner for an outside of a construction building.

It should say
THE CARROWFIELD
100 Carrowfield Street, East Boston – A Boutique Collection of Four Luxury Residences

Experience refined living with elegant design, high-end finishes, and expansive private decks in every residence. Thoughtfully crafted for both comfort and sophistication, each home features a modern fireplace and exceptional attention to detail.

Residence One – 2 Bed | 3 Bath | Private Yard + Large Deck
Residence Two – 2 Bed | 2 Bath | Spacious Deck
Residence Three – 2 Bed | 2 Bath | Expansive Deck
Residence Four – 2 Bed | 2 Bath | Panoramic Roof Deck with Stunning Boston Views
Now Accepting Reservations – Limited Availability

Schedule Your Private Tour Today

Marisa Thornquist, Larkspur Realty | 617-555-0192 | marisa@larkspurhomesmail.com
Construction by Pine Arch Builders

Target Market(s)

ages 30-50

Industry/Entity Type

real estate

Font styles to use
Serif

Requirements
Must have
• classic look
Nice to have
• colors of navy and gold

```html
<!DOCTYPE html>
<html lang="en">
<head>
<meta charset="utf-8">
<title>The Carrowfield – Luxury Residences Banner</title>
<link href="https://fonts.googleapis.com/css2?family=Cormorant+Garamond:wght@500;600&family=Libre+Caslon+Text:wght@400;700&family=Playfair+Display:ital,wght@1,600&display=swap" rel="stylesheet">
<style>
  :root {
    --navy: #243356;
    --navy-deep: #1b2a49;
    --band-dark: #18222f;
    --gold: #d4a862;
    --gold-soft: #c99d55;
    --ivory: #f4f1ea;
    --white: #ffffff;
    --ink: #2a3340;
    --muted: #7a7f88;
  }
  * { margin: 0; padding: 0; box-sizing: border-box; }
  html, body { width: 1200px; height: 480px; overflow: hidden; background: var(--white); }
  .banner {
    position: relative;
    width: 1200px;
    height: 480px;
    overflow: hidden;
    font-family: "Libre Caslon Text", Georgia, serif;
    color: var(--ivory);
  }
  .hero {
    position: absolute; left: 0; top: 0; width: 1200px; height: 267px;
    background: radial-gradient(ellipse at 50% 40%, #2a3b62 0%, var(--navy) 55%, var(--navy-deep) 100%);
  }
  .hero-texture { position: absolute; inset: 0; }
  .title {
    position: absolute; left: 0; width: 1200px; top: 20px;
    text-align: center;
    font-family: "Cormorant Garamond", Georgia, serif;
    font-weight: 600;
    font-size: 84px;
    line-height: 1;
    font-variant: small-caps;
    letter-spacing: 0;
    color: var(--white);
    text-shadow: 0 3px 6px rgba(0,0,0,0.35);
  }
  .title-rule {
    position: absolute; left: 296px; top: 120px; width: 610px; height: 2px;
    background: linear-gradient(90deg, transparent, var(--gold) 15%, var(--gold) 85%, transparent);
  }
  .brand {
    position: absolute; left: 1010px; top: 38px; width: 160px; text-align: center;
  }
  .brand-circle {
    display: block; margin: 0 auto 6px; width: 52px; height: 52px;
    border: 2px solid var(--gold); border-radius: 50%;
  }
  .brand-name {
    font-family: "Libre Caslon Text", Georgia, serif; font-weight: 400;
    font-size: 15px; letter-spacing: 1.5px; line-height: 1.3; color: var(--gold);
  }
  .address {
    position: absolute; left: 0; width: 1200px; top: 136px;
    text-align: center; font-size: 21px; color: var(--ivory);
  }
  .address svg { width: 12px; height: 16px; vertical-align: -1px; margin-right: 10px; }
  .tagline {
    position: absolute; left: 0; width: 1200px; top: 165px;
    text-align: center;
    font-family: "Playfair Display", Georgia, serif; font-style: italic; font-weight: 600;
    font-size: 33px; color: var(--white);
    text-shadow: 0 2px 5px rgba(0,0,0,0.35);
  }
  .intro {
    position: absolute; left: 110px; width: 980px; top: 208px;
    text-align: center; font-size: 14.6px; line-height: 20px; color: var(--ivory);
  }
  .residences {
    position: absolute; left: 0; top: 267px; width: 1200px; height: 100px;
    background: var(--band-dark);
  }
  .residence { position: absolute; top: 20px; text-align: center; }
  .residence-name { font-size: 22px; color: var(--gold); line-height: 1.1; margin-bottom: 6px; }
  .residence-specs { font-size: 14px; line-height: 18px; color: var(--ivory); white-space: nowrap; }
  .residence-specs .sep { color: var(--gold-soft); margin: 0 5px; }
  .r1 { left: 23px; width: 320px; }
  .r2 { left: 343px; width: 256px; }
  .r3 { left: 599px; width: 268px; }
  .r4 { left: 867px; width: 320px; }
  .col-divider {
    position: absolute; top: 22px; width: 1px; height: 60px;
    background: linear-gradient(180deg, transparent, var(--gold) 30%, var(--gold) 70%, transparent);
  }
  .cta-band {
    position: absolute; left: 0; top: 367px; width: 1200px; height: 42px; background: var(--navy);
  }
  .cta-tab { position: absolute; left: 0; top: 0; }
  .cta-text {
    position: absolute; left: 29px; top: 6px;
    font-family: "Cormorant Garamond", Georgia, serif; font-size: 24px; font-weight: 700;
    color: var(--white);
  }
  .availability {
    position: absolute; left: 540px; width: 560px; top: 8px; text-align: center;
    font-size: 21px; color: var(--ivory); white-space: nowrap;
  }
  .availability .accent { color: var(--gold); }
  .contact-strip {
    position: absolute; left: 0; top: 409px; width: 1200px; height: 57px; background: var(--white);
  }
  .contact {
    position: absolute; left: 29px; top: 15px; font-size: 21px; color: var(--ink); white-space: nowrap;
  }
  .contact .sep { color: var(--gold); margin: 0 10px; }
  .builder {
    position: absolute; right: 34px; top: 18px; white-space: nowrap; text-align: right;
  }
  .builder-by { font-size: 16px; color: var(--muted); margin-right: 14px; }
  .builder-name { font-size: 16px; color: var(--navy); letter-spacing: 0.5px; }
  .base-strip { position: absolute; left: 0; top: 466px; width: 1200px; height: 14px; background: var(--navy); }
</style>
</head>
<body>
<div class="banner">
  <section class="hero">
    <div class="hero-texture" role="img" aria-label="Subtle herringbone parquet texture in navy tones"></div>
    <h1 class="title">The Carrowfield</h1>
    <div class="title-rule"></div>
    <div class="brand">
      <span class="brand-circle"></span>
      <div class="brand-name">LARKSPUR<br>REALTY</div>
    </div>
    <p class="address">
      <svg viewBox="0 0 12 16" aria-hidden="true"><path d="M6 0C2.7 0 0 2.6 0 5.8 0 10 6 16 6 16s6-6 6-10.2C12 2.6 9.3 0 6 0zm0 8.2A2.4 2.4 0 1 1 6 3.4a2.4 2.4 0 0 1 0 4.8z" fill="#d4a862"/></svg>100 Carrowfield Street, East Boston
    </p>
    <h2 class="tagline">A Boutique Collection of Four Luxury Residences</h2>
    <p class="intro">Experience refined living with elegant design, high-end finishes, and expansive private decks in every residence. Thoughtfully crafted for<br>both comfort and sophistication, each home features a modern fireplace and exceptional attention to detail.</p>
  </section>

  <section class="residences">
    <div class="residence r1">
      <div class="residence-name">Residence 1</div>
      <div class="residence-specs">2 Bed<span class="sep">|</span>3 Bath<span class="sep">|</span>Private Yard <span class="sep">+</span> Large Deck</div>
    </div>
    <div class="col-divider" style="left:342px"></div>
    <div class="residence r2">
      <div class="residence-name">Residence 2</div>
      <div class="residence-specs">2 Bed<span class="sep">|</span>2 Bath<span class="sep">|</span>Spacious Deck</div>
    </div>
    <div class="col-divider" style="left:599px"></div>
    <div class="residence r3">
      <div class="residence-name">Residence 3</div>
      <div class="residence-specs">2 Bed<span class="sep">|</span>2 Bath<span class="sep">|</span>Expansive Deck</div>
    </div>
    <div class="col-divider" style="left:867px"></div>
    <div class="residence r4">
      <div class="residence-name">Residence 4</div>
      <div class="residence-specs">2 Bed<span class="sep">|</span>2 Bath<span class="sep">|</span>Panoramic Roof Deck<br>with Stunning Boston Views</div>
    </div>
  </section>

  <section class="cta-band">
    <svg class="cta-tab" width="450" height="42" viewBox="0 0 450 42" aria-hidden="true">
      <path d="M0 0 H446 C428 2 424 14 422 26 C420 36 414 42 400 42 H0 Z" fill="#d4a862"/>
    </svg>
    <p class="cta-text">Schedule Your Private Tour Today!</p>
    <p class="availability">Now Accepting Reservations &nbsp;- &nbsp;<span class="accent">Limited Availability</span></p>
  </section>

  <section class="contact-strip">
    <p class="contact">Marisa Thornquist<span class="sep">|</span>(617) 555-0192<span class="sep">|</span>marisa@larkspurhomesmail.com</p>
    <p class="builder"><span class="builder-by">by</span><span class="builder-name">PINE ARCH BUILDERS</span></p>
  </section>
  <div class="base-strip"></div>
</div>
</body>
</html>
```